Business logo & card design needed

We need a business logo & card design for a new company in NSW called 'Tallow Ridge Solutions'.
The company provides electrical services such as; electrical/refrigeration & air conditioning/data/security/audio visual entertainment/design & install.
We would like a logo which can relate to the electrical industry.
Updates

Industry/Entity Type

Electrical

Contact Information for Business Card

Tallow Ridge Solutions
Lira Mostfeld, Ph: 0471958360, Lic: 562930K

Logo Text

Tallow Ridge Solutions

Logo styles of interest
Emblem Logo
Abstract Logo
Wordmark Logo
Requirements
Must have
• The card must include the services we provide; electrical/refrigeration & air conditioning/data/security/audio visual entertainment/design & install.
It must also include the licence number; Lic: 562930K

```html
<!DOCTYPE html>
<html lang="en">
<head>
<meta charset="utf-8">
<title>Tallow Ridge Solutions – Business Card</title>
<link rel="stylesheet" href="https://fonts.googleapis.com/css2?family=Michroma&display=swap">
<style>
  :root {
    --canvas-bg: #2b2b2b;
    --card-dark: #0d0d0d;
    --card-light: #f7f7f7;
    --brand-red: #e3202a;
    --ink-dark: #1a1a1a;
    --ink-light: #ffffff;
  }
  * { box-sizing: border-box; margin: 0; padding: 0; }
  html, body {
    width: 1200px;
    height: 900px;
    overflow: hidden;
  }
  body {
    background: var(--canvas-bg);
    font-family: "Michroma", "Eurostile", sans-serif;
    display: flex;
    align-items: center;
    justify-content: center;
    gap: 56px;
  }
  .card {
    width: 500px;
    height: 290px;
    border-radius: 26px;
    display: flex;
    flex-direction: column;
    align-items: center;
    justify-content: center;
    box-shadow: 0 18px 40px rgba(0,0,0,0.45);
  }
  .card--front { background: var(--card-dark); }
  .card--back  { background: var(--card-light); }

  .brand-mark {
    width: 96px;
    height: 96px;
    border-radius: 50%;
    background: var(--brand-red);
  }
  .card--back .brand-mark { width: 78px; height: 78px; }

  .brand-name {
    margin-top: 18px;
    font-size: 17px;
    letter-spacing: 0.5px;
    color: var(--ink-light);
    text-transform: uppercase;
  }
  .card--back .brand-name {
    margin-top: 10px;
    font-size: 11px;
    color: var(--ink-dark);
  }

  .contact-name {
    margin-top: 12px;
    font-size: 15px;
    color: var(--ink-dark);
    text-transform: uppercase;
    letter-spacing: 0.5px;
  }
  .contact-line {
    margin-top: 6px;
    font-size: 12px;
    color: var(--ink-dark);
  }
  .contact-line .label { color: var(--brand-red); }
  .contact-line .item + .item { margin-left: 18px; }

  .services {
    margin-top: 12px;
    font-size: 8.5px;
    line-height: 1.7;
    text-align: center;
    color: var(--ink-dark);
    text-transform: uppercase;
  }
  .services .sep { color: var(--brand-red); padding: 0 3px; }
</style>
</head>
<body>
  <section class="card card--front">
    <div class="brand-mark" aria-hidden="true"></div>
    <h1 class="brand-name">Tallow Ridge Solutions</h1>
  </section>

  <section class="card card--back">
    <div class="brand-mark" aria-hidden="true"></div>
    <p class="brand-name">Tallow Ridge Solutions</p>
    <h2 class="contact-name">Lira Mostfeld</h2>
    <p class="contact-line">
      <span class="item"><span class="label">PH:</span> 0471958360</span>
      <span class="item"><span class="label">LIC:</span> 562930K</span>
    </p>
    <p class="services">
      Electrical<span class="sep">|</span>Refrigeration &amp; Air Conditioning<span class="sep">|</span>Data<br>
      Security<span class="sep">|</span>Audio Visual Entertainment<span class="sep">|</span>Design &amp; Install
    </p>
  </section>
</body>
</html>
```